we are an outdoor outlet in a country club that has a variety of outlets. The Club is called Brookhaven and is located in Cairo, Egypt. This garden menu will include cuisines from the Mediterranean, Asia and Texmex. we need a menu that is colorful and would fit an A3 size, back and front are to be used. Attached is the old menu currently in use (Garden Menu 2012.pdf is just for reference) and the new menu text for you to use is under the name Garden Menu Fall 2013
thank you.

```html
<!DOCTYPE html>
<html lang="en">
<head>
<meta charset="utf-8">
<title>Brookhaven Garden Menu</title>
<link href="https://fonts.googleapis.com/css2?family=Roboto+Condensed:wght@400;700&display=swap" rel="stylesheet">
<style>
  :root {
    --paper: #ffffff;
    --red: #a71c21;
    --green-dark: #5e7b2b;
    --green-light: #8fab3d;
    --ink: #ffffff;
    --rule: rgba(255,255,255,0.75);
  }
  * { margin: 0; padding: 0; box-sizing: border-box; }
  html, body { width: 1200px; height: 865px; overflow: hidden; background: var(--paper); }
  .menu-spread {
    position: relative; width: 1200px; height: 865px; overflow: hidden;
    font-family: "Roboto Condensed", "Arial Narrow", sans-serif; color: var(--ink);
  }
  .panel-shapes { position: absolute; inset: 0; }
  .column { position: absolute; }
  .section-title {
    text-align: center; font-size: 15px; font-weight: 400; text-transform: uppercase;
    line-height: 17px; margin: 4px 0 4px; letter-spacing: 0.2px;
  }
  .section-title.strong { font-weight: 700; font-size: 14px; }
  .group-title { font-weight: 700; font-size: 11.5px; line-height: 13px; margin-top: 2px; }
  .dish { margin-bottom: 7px; }
  .dish-name { font-size: 11.5px; line-height: 13.5px; }
  .dish-name small { font-size: 9px; }
  .dish-desc { font-size: 8.4px; line-height: 10px; opacity: 0.95; }
  .column-rule { position: absolute; width: 1px; background: var(--rule); }
  .dessert-list { list-style: none; font-size: 11.5px; line-height: 13.7px; }
</style>
</head>
<body>
<main class="menu-spread">
  <svg class="panel-shapes" width="1200" height="865" viewBox="0 0 1200 865" aria-hidden="true">
    <defs>
      <filter id="panel-shadow" x="-5%" y="-5%" width="110%" height="115%">
        <feDropShadow dx="3" dy="5" stdDeviation="4" flood-color="#000" flood-opacity="0.25"/>
      </filter>
    </defs>
    <rect x="600" y="27" width="570" height="811" fill="var(--green-light)" filter="url(#panel-shadow)"/>
    <path fill="var(--red)" filter="url(#panel-shadow)"
      d="M27,838 V200 C27,176 48,168 92,168 C140,168 185,171 200,176 C200,130 222,100 262,100 C288,100 304,108 312,120 C322,108 338,100 366,100 C404,100 422,132 424,178 C470,170 560,166 590,172 C600,176 600,185 600,190 V838 Z"/>
    <path fill="var(--green-dark)"
      d="M600,838 V200 C600,176 621,168 665,168 C713,168 758,171 773,176 C773,130 795,100 835,100 C861,100 877,108 885,120 C895,108 911,100 939,100 C977,100 995,132 997,178 C1043,170 1133,166 1163,172 C1170,176 1170,185 1170,190 V838 Z"/>
  </svg>

  <!-- Mediterranean panel, first column -->
  <section class="column" style="left:86px; top:246px; width:220px;">
    <h2 class="section-title strong">Soups</h2>
    <div class="dish"><p class="dish-name">Tomato Basil</p><p class="dish-desc">Simmered tomato soup finished with<br>fresh basil and cream</p></div>
    <div class="dish"><p class="dish-name">Chicken Cream</p><p class="dish-desc">Chicken broth with roasted chicken<br>cubes, pine nuts, and cream</p></div>
    <div class="dish"><p class="dish-name">Moroccan Harira</p><p class="dish-desc">Vegetable broth with fresh tomato,<br>chickpeas, lentil, cilantro,<br>and diced lamb</p></div>
    <h2 class="section-title strong">Appetizers</h2>
    <div class="dish"><p class="dish-name">Salmontartare</p><p class="dish-desc">seasoned with lemon juice, garlic, and<br>crushed black pepper</p></div>
    <div class="dish"><p class="dish-name">Roasted eggplant rolls</p><p class="dish-desc">with herbed ricotta cheese and pine nuts</p></div>
    <div class="dish"><p class="dish-name">Falafel in mini pita</p><p class="dish-desc">served with tehina and oriental salsa</p></div>
    <div class="dish"><p class="dish-name">Mankousha</p><p class="dish-desc">with thyme and olive oil</p></div>
    <div class="dish"><p class="dish-name">Fried kobeba</p><p class="dish-desc">with minced meat, spices, and pine nuts</p></div>
    <div class="dish"><p class="dish-name">Fried calamari a la Romana</p><p class="dish-desc">served with aioli</p></div>
    <div class="dish"><p class="dish-name">Samboussek</p><p class="dish-desc">with herbed white cheese and mint</p></div>
    <div class="dish"><p class="dish-name">Oriental sausage</p><p class="dish-desc">sautéed with garlic and onion</p></div>
    <div class="dish"><p class="dish-name">Mini vine leaves <small>with a yoghurt dip</small></p><p class="dish-desc">Fatouch with a pomegranate syrup dressing</p></div>
    <div class="dish"><p class="dish-name">Hummus seasoned</p><p class="dish-desc">with lemon juice, garlic, and olive oil</p></div>
    <div class="dish"><p class="dish-name">White cheese</p><p class="dish-desc">with diced tomato, thyme, and olive oil</p></div>
    <div class="dish"><p class="dish-name">Tehina</p><p class="dish-desc">seasoned with cumin, lemon juice, and garlic</p></div>
  </section>
  <div class="column-rule" style="left:313px; top:248px; height:532px;"></div>

  <!-- Mediterranean panel, second column -->
  <section class="column" style="left:334px; top:257px; width:232px;">
    <h2 class="section-title strong">Salads</h2>
    <div class="dish"><p class="dish-name">Caprese</p><p class="dish-desc">Buffalo mozzarella and sliced tomato with<br>a balsamic vinaigrette</p></div>
    <div class="dish"><p class="dish-name">Rocket Apple</p><p class="dish-desc">Rocket leaves with gorgonzola, croutons,<br>and strawberry vinaigrette</p></div>
    <div class="dish"><p class="dish-name">French Riviera Nicoise</p><p class="dish-desc">Lettuce, egg, tomato, tuna, olives, onion,<br>celery, radish, bell pepper in a French vinaigrette</p></div>
    <div class="dish"><p class="dish-name">Folle</p><p class="dish-desc">Mixed greens with crab sticks, mushroom,<br>corn, cherry tomato in a mango vinaigrette</p></div>
    <h2 class="section-title">Pizza &amp; Pasta</h2>
    <div class="dish"><p class="dish-name">Pizza Margarita <small>(Choose your toppings)</small></p><p class="dish-desc">Create your own pasta<br>Type:Spaghetti, Tagliatelle, Penne<br>Sauces: Napolitana, Bolognese, Alfredo</p></div>
    <h2 class="section-title" style="margin-top:12px;">Toppings</h2>
    <div class="dish"><p class="dish-desc">Bell peppers, olives, tomato, onion<br>Mushroom, chicken, tuna, pepperoni<br>Smoked salmon, shrimps<br>Lasagna</p></div>
    <h2 class="section-title" style="margin-top:12px;">Sandwiches</h2>
    <div class="dish"><p class="dish-desc">(Served with French fries or a garden salad)<br>Beef or chicken Shawerma</p></div>
    <div class="dish"><p class="dish-name">Grilled kofta</p><p class="dish-desc">Greek lamb gyro in pita bread with Tzatziki<br>Club sandwichwith smoked beef, turkey, egg</p></div>
    <h2 class="section-title" style="text-align:left; margin-top:8px;">Main Courses</h2>
    <div class="dish"><p class="dish-name">Veal Parmeggiana</p><p class="dish-desc">Breaded veal escalope topped with melted<br>cheese and tomato sauce served with Spaghetti</p></div>
    <div class="dish"><p class="dish-name">Chicken a la Francaise</p><p class="dish-desc">Pan fried chicken breast in a mushroom<br>cream sauce with vegetables white rice</p></div>
  </section>

  <!-- Asian panel column -->
  <section class="column" style="left:662px; top:247px; width:220px;">
    <div class="dish"><p class="dish-name">Grilled Salmon</p><p class="dish-desc">Salmon steak charcoal grilled with avocado<br>tomato relish and creamy mushroom risotto</p></div>
    <div class="dish"><p class="dish-name">Moroccan Chicken</p><p class="dish-desc">Chicken cubes simmered with spices and<br>olives served with tomato rice</p></div>
    <div class="dish"><p class="dish-name">Filet</p><p class="dish-desc">Tender filet grilled to your liking served with<br>mashed potato and creamed spinach</p></div>
    <div class="dish"><p class="dish-name">Choice of sauces</p><p class="dish-desc">Brown mushroom, Green Peppercorn, Gorgonzola</p></div>
    <h2 class="section-title" style="text-align:left; margin-top:8px;">Asian Corner</h2>
    <p class="group-title">Salads &amp; Appetizers:</p>
    <div class="dish"><p class="dish-name">Chicken Wasabi Salad</p><p class="dish-desc">Diced chicken with a mayo wasabi dressing<br>on top of shredded lettuce</p></div>
    <div class="dish"><p class="dish-name">Chicken Sesame Noodle Salad</p><p class="dish-desc">Sesame crusted chicken with glass noodles tossed<br>with sweet chili, soy sauce, and lemongrass</p></div>
    <div class="dish"><p class="dish-name">Spring rolls</p><p class="dish-desc">Vegetable spring rolls served with house<br>made sweet and sour dip</p></div>
    <div class="dish"><p class="dish-name">Indian Samosa</p><p class="dish-desc">Fried dough parcels filled with vegetables and spices</p></div>
    <p class="group-title">Main Courses:</p>
    <div class="dish"><p class="dish-name">Murgh Chicken Makhni</p><p class="dish-desc">Chicken cubes in a rich creamy tomato sauce<br>seasoned with garam masala</p></div>
    <div class="dish"><p class="dish-name">Choice of side</p><p class="dish-desc">vegetable korma or curd</p></div>
    <div class="dish"><p class="dish-name">Chicken Tandoori</p><p class="dish-desc">Grilled chicken cubes with tandoori spices<br>served with basmati rice</p></div>
    <div class="dish"><p class="dish-name">Thai Coconut Curry Shrimp</p><p class="dish-desc">Sautéed shrimp tossed with curry and<br>coconut milk served with jasmine rice</p></div>
    <div class="dish"><p class="dish-name">Mongolian Beef</p><p class="dish-desc">Soy marinated beef with oyster sauce and<br>vegetables served with egg noodles</p></div>
  </section>
  <div class="column-rule" style="left:887px; top:248px; height:545px;"></div>

  <!-- Tex Mex and desserts column -->
  <section class="column" style="left:907px; top:246px; width:215px;">
    <h2 class="section-title">Tex Mex</h2>
    <p class="group-title">Salads &amp; Appetizers:</p>
    <div class="dish"><p class="dish-name">Caesar Salad</p><p class="dish-desc">Iceberg lettuce with Caesar dressing with<br>grated Parmesan cheese and croutons</p></div>
    <div class="dish"><p class="dish-name">Taco salad42</p><p class="dish-desc">Chicken breast, beans, sour cream, guacamole,<br>tomato, corn, lettuce, olives, chives, vinaigrette<br>Nachos topped with chili, melted cheese, beans<br>Chicken Quesadilla served with guacamole,<br>salsa, and sour cream</p></div>
    <p class="group-title">Main Courses &amp; Sandwiches:</p>
    <div class="dish"><p class="dish-name">Cheeseburger</p><p class="dish-desc">House made lean beef burger topped with cheddar cheese</p></div>
    <div class="dish"><p class="dish-name">Mushroom Burger</p><p class="dish-desc">Beef burger with sautéed mushroom,<br>caramelized onion, and provolone cheese</p></div>
    <div class="dish"><p class="dish-name">Crispy Chicken Wrap</p><p class="dish-desc">Crisp fried chicken wrap with a ranch dressing<br>Fajita (Chicken, Beef, Combo)</p></div>
    <div class="dish"><p class="dish-name">Pan <span class="dish-desc">seared meat or chicken with onion and bell pepper</span></p><p class="dish-desc">served with sour cream, guacamole, salsa</p></div>
    <h2 class="section-title" style="margin-top:8px;">Desserts</h2>
    <ul class="dessert-list">
      <li>Mix Berries Cheesecake</li>
      <li>Crème Brulee</li>
      <li>Chocolate Caramel Cake</li>
      <li>Warm Chocolate Fondant</li>
      <li>Baked Apple Tart Tatin</li>
      <li>Tiramisu</li>
      <li>Pumpkin Pie Flan</li>
      <li>Mixed Berries Granola Yoghurt</li>
      <li>Vanilla Ice Cream Profiterole with dark and white chocolate sauce</li>
      <li>Caramelized Banana with Deep Fried Ice Cream</li>
      <li>Baklava with Nuts and Sugar Syrup</li>
      <li>Shot Glass Sampler – Tiramisu, Chocolate Crisp Mousse, Pear with Sabayon</li>
      <li>Ice Cream by Scoop</li>
    </ul>
  </section>
</main>
</body>
</html>
```